Website design for legal tech start up in Switzerland (B2B)

We are for a legal tech start up in Switzerland called TAVO. We have been running since August 2016. This will be our first live website.

We need a website designed and business card design for our start-up in Switzerland. We also need the Web design to be converted into HTML and CSS files.

Function of website:
• To inform potential customers of our services
• Form a key part of our digital marketing and sales footprint.
• Branding

Please find attached logo.
Updates

Project Deadline Extended Reason: Giving us time to review submissions and provide opportunity for more submissions. Added Thursday, February 16, 2017

Reason: Looking for more idea's not necessarily set on blue and grey colours only.

Target Market(s)

B2B tech powered legal services.

Industry/Entity Type

Legal

Contact Information for Business Card

Lean and slick design.

Coding

Coded - Design and coding required

Number of Pages Required

5+ page

Requirements
Must have
• VERY LEAN AND CLEAN DESIGN!
• We have received many great standard designs, but we are looking for something more out-of-the box: You can get inspiration from these designs: http://www.pindelsite.com/websites/clean/
• Thanks!!
• Easy content management system
• Well structured coding for additional development
• Responsive webpage for all types of devices
• SEO optimized
• Tabs (Home, services, team, careers, blog, contact us)
• Colour scheme complementary to logo
Nice to have
• Look and Design - Approachable, High-tech, Modern
• Easy to add chat bot capability in future
Should not have
• Too busy/ too much clutter
• Not take to long to load

```html
<!DOCTYPE html>
<html lang="en">
<head>
<meta charset="utf-8">
<title>TAVO – Business Card</title>
<link rel="stylesheet" href="https://fonts.googleapis.com/css2?family=Arimo:wght@700&family=Open+Sans:wght@400&display=swap">
<style>
  :root {
    --navy: #2e2f61;
    --charcoal: #48454a;
    --text: #4a4a4a;
    --rule: #e6e6e6;
    --paper: #ffffff;
  }
  * { margin: 0; padding: 0; box-sizing: border-box; }
  html, body {
    width: 1200px;
    height: 720px;
    overflow: hidden;
    background: var(--paper);
  }
  .card {
    position: relative;
    width: 1200px;
    height: 720px;
    background: var(--paper);
    overflow: hidden;
  }
  .card__band {
    position: absolute;
    inset: 0;
    width: 1200px;
    height: 720px;
  }
  .brand {
    position: absolute;
    left: 72px;
    top: 96px;
    font-family: "Arimo", Arial, sans-serif;
    font-weight: 700;
    font-size: 142px;
    line-height: 1;
    letter-spacing: 6px;
    color: var(--charcoal);
  }
  .person {
    position: absolute;
    left: 74px;
    top: 516px;
    font-family: "Arimo", Arial, sans-serif;
    font-weight: 700;
  }
  .person__name {
    font-size: 39px;
    letter-spacing: 1.5px;
    color: var(--navy);
    line-height: 1;
  }
  .person__role {
    margin-top: 22px;
    font-size: 19px;
    letter-spacing: 0.8px;
    color: var(--text);
    line-height: 1;
  }
  .contact {
    position: absolute;
    left: 721px;
    top: 326px;
    width: 404px;
    list-style: none;
    font-family: "Open Sans", Arial, sans-serif;
    color: var(--text);
  }
  .contact__item {
    display: flex;
    align-items: center;
    gap: 18px;
    height: 66px;
    font-size: 25px;
    border-bottom: 1px solid var(--rule);
  }
  .contact__item + .contact__item { height: 72px; }
  .contact__item:nth-child(3) { height: 66px; }
  .contact__item:last-child {
    border-bottom: none;
    font-size: 22px;
    height: 68px;
  }
  .contact__icon {
    width: 24px;
    height: 24px;
    flex: none;
    fill: var(--charcoal);
  }
</style>
</head>
<body>
  <main class="card">
    <svg class="card__band" viewBox="0 0 1200 720" aria-hidden="true">
      <polygon fill="var(--navy)" points="741,55 1200,55 1200,146 741,146 504,413 0,413 0,323 504,323"/>
    </svg>

    <div class="brand">TAVO</div>

    <section class="person">
      <h1 class="person__name">MARCO BRUNNER</h1>
      <p class="person__role">BUSINESS DEVELOPMENT</p>
    </section>

    <ul class="contact">
      <li class="contact__item">
        <svg class="contact__icon" viewBox="0 0 24 24" aria-hidden="true">
          <rect x="1" y="1" width="22" height="22" rx="4"/>
          <path fill="#fff" d="M8 5.5c.6 0 1.5 2.3 1.5 2.8 0 .8-1.2 1.2-1 1.9.5 1.6 2.4 3.6 4 4.2.7.3 1.2-.9 2-.9.5 0 2.6 1 2.6 1.6 0 1.5-1.4 2.6-2.8 2.4C10 17 6.8 13.6 6 9.5 5.6 7.6 6.6 5.5 8 5.5z"/>
        </svg>
        <span>0123 456 789</span>
      </li>
      <li class="contact__item">
        <svg class="contact__icon" viewBox="0 0 24 24" aria-hidden="true">
          <path d="M1 5h22v2l-11 7L1 7z"/>
          <path d="M1 9l11 7 11-7v10H1z"/>
        </svg>
        <span>info@tavo.com.au</span>
      </li>
      <li class="contact__item">
        <svg class="contact__icon" viewBox="0 0 24 24" aria-hidden="true">
          <circle cx="12" cy="12" r="11"/>
          <path fill="#fff" d="M6 6c2 0 3 1 4 2s-1 2-2 3 0 3 1 4-1 3-2 2-2-4-3-6 0-4 2-5zM14 4c2 1 2 2 1 3s1 2 3 2 2 3 1 5-2 4-3 3 0-3-1-4-3-1-3-3 2-2 2-3-2-2 0-3z"/>
        </svg>
        <span>www.tavo.com.au</span>
      </li>
      <li class="contact__item">
        <svg class="contact__icon" viewBox="0 0 24 24" aria-hidden="true">
          <path d="M12 3L1 12.5h3V21h6v-6h4v6h6v-8.5h3z"/>
        </svg>
        <span>Lorem Ipsum is simply dummy text</span>
      </li>
    </ul>
  </main>
</body>
</html>
```